Small Catering Menu

I am looking to make a small menu for catering for my company. I am thinking of a small A5 size booklet which will also have some pictures and the cover needs to be attractive.
Likely to be 8-12 pages depending upon your design (could be less or more). I need 2-3 pages as proposal concept (Cover, inside first page and one menu page) and if we like it we will make the project guaranteed before finishing the rest of the project to add security for the designer.
Pictures will be provided to the designer whose concept is the best as they are too heavy. But use generic photos for now (rather large ones) if possible.
Logo is available and so is the inside text as well as some other tidbits.
I will provide the fonts too to ensure it maintains the corporate integrity that we are following.
Industry/Entity Type
Catering

```html
<!DOCTYPE html>
<html lang="en">
<head>
<meta charset="utf-8">
<title>Harbor Table Catering – Menu Cover</title>
<link href="https://fonts.googleapis.com/css2?family=Montserrat:wght@300;400;700&family=Great+Vibes&display=swap" rel="stylesheet">
<style>
  :root {
    --page-bg: #e9e8e4;
    --ink: #1a1a1a;
    --gold: #cf9a32;
    --panel: rgba(248, 244, 238, 0.86);
    --photo-dark: #4a2a14;
    --photo-mid: #9a5f34;
    --photo-light: #c98f5e;
    --wood: #8a6244;
    --berry: #b3261e;
    --white: #ffffff;
  }
  * { margin: 0; padding: 0; box-sizing: border-box; }
  html, body {
    width: 1200px; height: 1000px; overflow: hidden;
    background: var(--page-bg);
    font-family: "Montserrat", Arial, sans-serif;
  }
  .canvas {
    position: relative; width: 1200px; height: 1000px;
    display: flex; align-items: center; justify-content: center;
  }
  .cover {
    position: relative; width: 664px; height: 940px; overflow: hidden;
    box-shadow: 0 6px 18px rgba(0,0,0,0.25);
  }
  .cover-photo {
    position: absolute; inset: 0;
    background:
      radial-gradient(ellipse 40% 18% at 30% 78%, rgba(179,38,30,0.55), transparent 70%),
      linear-gradient(180deg, var(--photo-dark) 0%, var(--photo-mid) 22%, var(--photo-light) 45%, #b98760 62%, var(--wood) 80%, #4a3020 100%);
  }
  .brand-panel {
    position: absolute; left: 58px; top: 150px; width: 580px; height: 470px;
    background: var(--panel);
    display: flex; flex-direction: column; align-items: center;
  }
  .brand-name {
    margin-top: 150px;
    display: flex; align-items: center; gap: 14px;
    font-weight: 700; font-size: 44px; letter-spacing: 1px;
    color: var(--ink);
  }
  .brand-mark {
    width: 22px; height: 22px; background: var(--gold);
  }
  .brand-tagline {
    margin-top: 14px;
    font-family: "Great Vibes", cursive;
    font-size: 130px; line-height: 1; color: var(--ink);
  }
  .contact {
    position: absolute; left: 230px; top: 655px; width: 380px;
    text-align: center; color: var(--white);
  }
  .contact-phone { font-weight: 300; font-size: 34px; letter-spacing: 0.5px; }
  .contact-line { font-weight: 300; font-size: 13px; line-height: 1.4; }
  .rule {
    position: absolute; left: 250px; top: 790px; width: 380px; height: 1px;
    background: rgba(255,255,255,0.85);
  }
  .website {
    position: absolute; left: 250px; top: 812px; width: 380px;
    text-align: center; color: var(--white);
    font-size: 16px; font-weight: 400; letter-spacing: 6px;
  }
</style>
</head>
<body>
  <main class="canvas">
    <article class="cover">
      <div class="cover-photo" role="img" aria-label="Photo of fresh strawberries in a white bowl with syrup drizzle on a rustic wooden board"></div>
      <section class="brand-panel">
        <div class="brand-name"><span class="brand-mark"></span>HARBOR TABLE</div>
        <div class="brand-tagline">Catering</div>
      </section>
      <section class="contact">
        <div class="contact-phone">800-123-4567</div>
        <div class="contact-line">contact@email.com</div>
        <div class="contact-line">www.domainname.com</div>
      </section>
      <div class="rule"></div>
      <div class="website">www.websitehere.com</div>
    </article>
  </main>
</body>
</html>
```